Online trading school - Website design

We are building an online trading school (trading of shares, commodities, indices, currencies). The purpose is to teach online traders how to trade successfully. We need to design the homepage of the website and logo (bramwelloq.com will be the domain). The homepage will contain the following elements

- logo
- Sign in and Register links/buttons
- upper menu
- short introduction
- a couple of bullet points 'Why to join our school?'
- sign up form
- text
- bottom menu

Attached is a draft for the designer. The draft is just for an inspiration, the actual structure of the website can be different if the designer thinks so.

The designer is free to choose colors.

School

3 page

```html
<!DOCTYPE html>
<html lang="en">
<head>
<meta charset="utf-8">
<title>Bramwelloq – Online Trading School</title>
<link href="https://fonts.googleapis.com/css2?family=Raleway:wght@400;500;600;700&family=Yanone+Kaffeesatz:wght@400&display=swap" rel="stylesheet">
<style>
:root{
  --orange:#f08a0a;
  --orange-band:#f4a03c;
  --panel:#3a3a3a;
  --input:#2a2a2a;
  --text:#555;
  --heading:#4a4a4a;
  --list:#3d3325;
  --white:#fff;
  --rule:#8a8a8a;
}
*{margin:0;padding:0;box-sizing:border-box}
html,body{width:972px;height:1200px;overflow:hidden;background:var(--white);font-family:"Raleway",sans-serif}
.page{position:relative;width:972px;height:1200px}
.abs{position:absolute}
.hero-bg{left:0;top:0;width:972px;height:414px;background:linear-gradient(180deg,#1c1412 0%,#2a1d18 40%,#1e1a1c 100%)}
.brand{left:74px;top:31px;font-family:"Raleway",sans-serif;font-weight:600;font-size:30px;color:var(--orange);letter-spacing:1px;line-height:1}
.btn-top{top:8px;height:21px;width:72px;background:var(--orange);color:#5a2a00;font-size:12px;font-weight:600;text-align:center;line-height:21px;border:1px solid #c46f00}
.social{top:12px;color:var(--white);font-size:9px;font-weight:600;line-height:12px}
.nav a{position:absolute;top:45px;height:21px;line-height:21px;color:var(--white);font-size:12px;font-weight:500;text-decoration:none;white-space:nowrap}
.nav a.active{background:var(--white);color:var(--orange);padding:0 8px;font-weight:600;border-radius:2px}
.form{left:73px;top:105px;width:181px;height:249px;background:var(--panel)}
.form-title{height:33px;line-height:33px;text-align:center;color:#eee;font-size:14px;font-weight:600;border-bottom:2px solid #555;background:#444}
.field{position:absolute;left:14px;width:152px;height:25px;background:var(--input);color:#ccc;font-size:10px;padding-left:9px;line-height:25px;border-bottom:1px solid #555}
.check{left:14px;top:156px;width:10px;height:10px;background:var(--white)}
.terms{left:36px;top:156px;color:#ccc;font-size:9.5px;line-height:12px}
.submit{left:43px;top:195px;width:94px;height:31px;background:var(--orange);color:#6a3400;font-size:13px;font-weight:700;text-align:center;line-height:27px;border:2px solid #222}
.slide-frame{left:284px;top:82px;width:616px;height:302px;background:#f4f4f4;box-shadow:0 2px 6px rgba(0,0,0,.4);transform:rotate(-.3deg)}
.slide{left:295px;top:100px;width:591px;height:265px;background:linear-gradient(135deg,#dfe4ea,#b9c3cf 50%,#eef0f2)}
.arrow{top:226px;width:10px;height:14px}
h2.title{position:absolute;left:0;width:972px;text-align:center;font-family:"Yanone Kaffeesatz",sans-serif;font-weight:400;font-size:30px;color:var(--heading)}
.title .name{color:var(--orange)}
.rule{height:4px;border-top:1px solid var(--rule);border-bottom:1px solid var(--rule)}
.para{color:var(--text);font-size:10.5px;line-height:18.8px}
.readmore{left:440px;top:583px;width:102px;height:29px;background:var(--orange);color:#6a3400;font-size:14px;font-weight:700;text-align:center;line-height:27px;border:1px solid #8a4a00}
.band{left:0;top:650px;width:972px;height:260px;background:var(--orange-band)}
.why-title{left:74px;top:686px;font-family:"Yanone Kaffeesatz",sans-serif;font-size:30px;color:#4e5060}
.why-list li{position:absolute;left:79px;list-style:none;color:var(--list);font-size:12px;font-weight:600;padding-left:23px;white-space:nowrap}
.why-list li::before{content:"";position:absolute;left:0;top:3px;width:8px;height:8px;border-radius:50%;border:1px solid #8a5a10;background:#c9821e}
.polaroid{top:690px;width:160px;height:180px;background:var(--white);box-shadow:1px 2px 3px rgba(0,0,0,.3)}
.polaroid .pic{position:absolute;left:8px;top:7px;width:144px;height:166px}
.footer{left:0;top:1150px;width:972px;height:50px;background:var(--orange-band)}
.copy{left:74px;top:1167px;font-size:10px;color:#3a2a10}
.foot-nav a{position:absolute;top:1166px;font-size:10px;color:#4a3a20;text-decoration:none;white-space:nowrap}
.foot-nav a.active{font-weight:600}
</style>
</head>
<body>
<div class="page">
  <div class="abs hero-bg" role="img" aria-label="Dark stock exchange ticker board background"></div>
  <div class="abs brand">BRAMWELLOQ</div>

  <div class="abs btn-top" style="left:679px">Sign in</div>
  <div class="abs btn-top" style="left:766px">Register</div>
  <span class="abs social" style="left:845px">Kolo</span>
  <span class="abs social" style="left:868px">Piva</span>
  <span class="abs social" style="left:891px">Zetra</span>

  <nav class="nav">
    <a class="active" style="left:456px">About Our School</a>
    <a style="left:589px">Risk Warning</a>
    <a style="left:688px">FAQ</a>
    <a style="left:735px">Trading Glossary</a>
    <a style="left:854px">Contact</a>
  </nav>

  <div class="abs form">
    <div class="form-title">Join Our School Now!</div>
    <div class="field" style="top:45px">First Name</div>
    <div class="field" style="top:85px">Last Name</div>
    <div class="field" style="top:122px">Email</div>
    <div class="abs check"></div>
    <div class="abs terms">Dagree with Our Tearms<br>And canditions</div>
    <div class="abs submit">Submit</div>
  </div>

  <div class="abs slide-frame"></div>
  <div class="abs slide" role="img" aria-label="Photo of a business team meeting around a table with papers and tablets"></div>
  <svg class="abs arrow" style="left:332px" viewBox="0 0 10 14"><path d="M8 1 2 7l6 6" fill="none" stroke="#f08a0a" stroke-width="2"/></svg>
  <svg class="abs arrow" style="left:832px" viewBox="0 0 10 14"><path d="M2 1l6 6-6 6" fill="none" stroke="#f08a0a" stroke-width="2"/></svg>

  <h2 class="title" style="top:450px">About Us <span class="name">Bramwelloq</span></h2>
  <div class="abs rule" style="left:330px;top:494px;width:312px"></div>
  <p class="abs para" style="left:79px;top:511px;width:814px;text-align:center">Lorem ipsum dolor sit amet, consectetuer adipiscing elit, sed diam nonummy nibh euismod tincidunt ut laoreet dolore magna aliquam erat volutpat. Ut wisi enim ad minim veniam,&nbsp; lobortis nisl ut aliquip ex ea commodo consequat. Duis autem vel eum iriure dolor in hendrerit in vulputate velit esse molestie eros et dignissim qui blandit praesent luptatum zzril delenit augue duis dolore te feugait nulla facilisi.</p>
  <div class="abs readmore">Read More</div>

  <div class="abs band"></div>
  <div class="abs why-title">Why To Join Us?</div>
  <div class="abs rule" style="left:74px;top:729px;width:254px;border-color:#8a6a40"></div>
  <ul class="why-list">
    <li style="top:748px">Best Trading Tips Ever</li>
    <li style="top:775px">Secret Tips From Experts</li>
    <li style="top:803px">We Teach You How To Trade Online</li>
    <li style="top:831px">Learn How to Trade Commodities</li>
    <li style="top:857px">Learn How to Become a Trader</li>
  </ul>
  <div class="abs polaroid" style="left:350px"><div class="pic" role="img" aria-label="Grains and stacks of coins" style="background:linear-gradient(135deg,#f0a040,#e8c070 50%,#b8a070)"></div></div>
  <div class="abs polaroid" style="left:542px"><div class="pic" role="img" aria-label="Hand pointing at a rising market chart on a tablet" style="background:linear-gradient(135deg,#1c3a5a,#2a6a9a 50%,#c04040)"></div></div>
  <div class="abs polaroid" style="left:733px"><div class="pic" role="img" aria-label="Gold currency symbols on puzzle pieces" style="background:linear-gradient(135deg,#ffffff,#e8e8e8 55%,#e0b040)"></div></div>

  <h2 class="title" style="top:944px">What Do We Offer?</h2>
  <div class="abs rule" style="left:330px;top:989px;width:312px"></div>
  <p class="abs para" style="left:74px;top:1004px;width:820px;line-height:19.6px;font-size:11px;text-indent:26px">Lorem ipsum dolor sit amet, consectetuer adipiscing elit, sed diam nonummy nibh euismod tincidunt ut laoreet dolore magna aliquam erat volutpat. Ut wisi enimminim veniam,&nbsp; lobortis nisl ut aliquip ex ea commodo consequat. Duis autem vel eum iriure dolor in hendrerit in vulputate velit esse molestie eros et dignissim qui blanfgfbgfraesent luptatum zzril delenit augue duis dolore te feugait nulla facilisi.</p>
  <p class="abs para" style="left:74px;top:1072px;width:820px;line-height:19.6px;font-size:11px;text-indent:26px">dolore magna aliquam erat volutpat. Ut wisi enimminim veniam,&nbsp; lobortis nisl ut aliquip ex ea commodo consequat. Duis autem vel eum iriure dolor in hendrerit in vulputate velit esse molestie eros et dignissim qui blanfgfbgfraesent luptatum zzril delenit augue duis dolore te feugait nulla facilisi.</p>

  <div class="abs footer"></div>
  <div class="abs copy">copyright © 2016 bramwelloq all rights reserved.</div>
  <nav class="foot-nav">
    <a class="active" style="left:544px">About Our School</a>
    <a style="left:646px">Risk Warning</a>
    <a style="left:725px">FAQ</a>
    <a style="left:762px">Trading Glossary</a>
    <a style="left:861px">Contact</a>
  </nav>
</div>
</body>
</html>
```